Business Card Design Project

We're looking for a unique business card design that stands out from the rest, using the brand and logo we've already developed.
Two-sided design please.
Brightvane Media (www.brightvanemedia.com.au) is a digitally-focused advertising agency that has produces results-driven campaigns. As a result, we'd like our business card to reflect our innovative approach.
Size, shape, orientation, etc, are all flexible (providing the print costs don't become ridiculous or we have to sit there with tiny scissors!).
Business card should include space for name, title, email, mobile, landline and address.
Logo files uploaded.

```html
<!DOCTYPE html>
<html lang="en">
<head>
<meta charset="utf-8">
<title>Brightvane Media – Business Card</title>
<link rel="stylesheet" href="https://fonts.googleapis.com/css2?family=Roboto:wght@400;500;700&display=swap">
<style>
  :root {
    --stage-light: #f7f7f8;
    --stage-dark: #dcdde0;
    --orange-bright: #f68a2c;
    --orange-deep: #d8521f;
    --orange-text: #f07f22;
    --ink: #2a2a2a;
    --card-white: #ffffff;
  }
  * { margin: 0; padding: 0; box-sizing: border-box; }
  html, body { width: 1200px; height: 900px; overflow: hidden; }
  body {
    position: relative;
    background: radial-gradient(ellipse at 50% 45%, var(--stage-light) 0%, var(--stage-dark) 100%);
    font-family: "Roboto", Arial, sans-serif;
    color: var(--ink);
  }
  .card {
    position: absolute;
    width: 500px;
    height: 286px;
    box-shadow: 0 6px 14px rgba(0, 0, 0, 0.18);
  }
  /* Front side */
  .card-front {
    left: 80px;
    top: 190px;
    background: radial-gradient(circle at 50% 48%, var(--orange-bright) 0%, #ec7426 45%, var(--orange-deep) 100%);
    display: flex;
    align-items: center;
    justify-content: center;
  }
  .front-wordmark {
    font-weight: 500;
    font-size: 46px;
    letter-spacing: 1px;
    color: var(--ink);
  }
  /* Back side */
  .card-back {
    left: 620px;
    top: 410px;
    background: var(--card-white);
  }
  .back-wordmark {
    position: absolute;
    top: 30px;
    right: 30px;
    font-weight: 500;
    font-size: 17px;
    color: var(--ink);
  }
  .contact-block {
    position: absolute;
    left: 34px;
    top: 70px;
    font-size: 14px;
    line-height: 1.3;
  }
  .person-name { color: var(--orange-text); font-weight: 700; font-size: 15px; }
  .person-title { color: var(--orange-text); font-size: 15px; margin-bottom: 14px; }
  .office-address { margin-bottom: 14px; }
  .contact-list { list-style: none; }
  .contact-list li { display: flex; gap: 10px; }
  .contact-label { color: var(--orange-text); width: 10px; }
</style>
</head>
<body>
  <section class="card card-front" aria-label="Business card front">
    <span class="front-wordmark">Brightvane Media</span>
  </section>

  <section class="card card-back" aria-label="Business card back">
    <span class="back-wordmark">Brightvane Media</span>
    <div class="contact-block">
      <p class="person-name">Daniel Hart</p>
      <p class="person-title">Managing Director</p>
      <p class="office-address">Brisbane Head Office<br>3/27 Larkfield St,<br>Ashgrove, Qld, 4060</p>
      <ul class="contact-list">
        <li><span class="contact-label">m</span>1300 482 915</li>
        <li><span class="contact-label">t</span>(07) 3391 2854</li>
        <li><span class="contact-label">e</span>daniel.hart@brightvane.com</li>
        <li><span class="contact-label">w</span>www.brightvanemedia.com.au</li>
      </ul>
    </div>
  </section>
</body>
</html>
```